Full service meeting planning company needs new business cards

Velmora Linkway is a full service meeting planning company that specializes in on-line conference registration web development and event communications. We combine citywide hotel management, mobile applications, eblast reminders, confirmation letters, and customized reporting to create a seamless registration process. We also manage group motor coach transportation, food and beverages, entertainment, stage and lighting for group of 10 to 4000.

Target Market(s)

Corporations and associations

Industry/Entity Type

Event Planning

Contact Information for Business Card

standard size 3.5" wide and 2" tall

Font styles to use
Serif
Sans Serif

Colors
f37122
f78f20
333333
5c5c5c
9d9d9d
f68d4d

Requirements
Must have
• {name}
• Velmora Linkway
• P.O. Box 7384, Grand Rapids, M I 49568
• www.velmoralinkway.com
• {email}
• {phone}
• {mobile phone}
Nice to have
• Our colors are black, grey and orange as an accent color
Should not have
• I am not happy with our website layout anymore either. It feels dark and old but it does explain who we are pretty well if you'd like to review; www.velmoralinkway.com

```html
<!DOCTYPE html>
<html lang="en">
<head>
<meta charset="utf-8">
<title>Velmora Linkway – Business Card</title>
<link rel="stylesheet" href="https://fonts.googleapis.com/css2?family=Montserrat:wght@600&family=PT+Sans:wght@400;700&display=swap">
<style>
  :root {
    --orange: #f37122;
    --orange-light: #f78f20;
    --card-black: #111111;
    --charcoal: #333333;
    --grey: #9d9d9d;
    --grey-light: #c7c5c5;
    --white: #ffffff;
    --backdrop: #e9e6e2;
  }
  * { margin: 0; padding: 0; box-sizing: border-box; }
  html, body { width: 1200px; height: 900px; overflow: hidden; }
  body {
    background: var(--backdrop);
    font-family: "PT Sans", Arial, sans-serif;
    position: relative;
  }
  .card {
    position: absolute;
    left: 250px;
    width: 700px;
    height: 400px;
    background: var(--card-black);
    box-shadow: 0 8px 22px rgba(0,0,0,0.25);
    overflow: hidden;
  }
  .card--front { top: 35px; }
  .card--back { top: 465px; }

  .brand { position: absolute; display: flex; flex-direction: column; align-items: center; z-index: 1; }
  .brand__dot { border-radius: 50%; background: var(--orange); }
  .brand__name {
    font-family: "Montserrat", "Century Gothic", sans-serif;
    font-weight: 600;
    color: var(--orange);
    text-transform: uppercase;
    white-space: nowrap;
  }
  .card--front .brand { left: 0; right: 0; top: 78px; }
  .card--front .brand__dot { width: 150px; height: 150px; }
  .card--front .brand__name { font-size: 29px; letter-spacing: 1px; margin-top: 24px; }

  .card--back .brand { right: 40px; top: 40px; }
  .card--back .brand__dot { width: 108px; height: 108px; }
  .card--back .brand__name { font-size: 20px; letter-spacing: 0.5px; margin-top: 12px; }

  .wave { position: absolute; inset: 0; width: 100%; height: 100%; }

  .person { position: absolute; left: 70px; top: 60px; color: var(--white); z-index: 1; }
  .person__name { font-size: 23px; font-weight: 700; color: var(--orange); line-height: 1.1; }
  .person__title { font-size: 16px; line-height: 1.2; }

  .contacts { position: absolute; left: 62px; top: 136px; list-style: none; color: var(--white); font-size: 18px; z-index: 1; }
  .contacts li { display: flex; align-items: center; gap: 10px; height: 25px; }
  .contacts svg { width: 16px; height: 16px; fill: var(--orange); flex: none; }

  .address { position: absolute; left: 84px; top: 226px; color: var(--white); font-size: 19px; line-height: 1.4; font-style: normal; z-index: 1; }

  .website { position: absolute; right: 38px; top: 262px; color: var(--white); font-size: 15px; z-index: 1; }
</style>
</head>
<body>

<section class="card card--front" aria-label="Card front">
  <div class="brand">
    <div class="brand__dot"></div>
    <div class="brand__name">Velmora Linkway</div>
  </div>
</section>

<section class="card card--back" aria-label="Card back">
  <svg class="wave" viewBox="0 0 700 400" preserveAspectRatio="none" aria-hidden="true">
    <path d="M0,305 C170,305 280,292 360,262 C430,236 480,240 560,244 L700,240 L700,400 L0,400 Z" fill="var(--grey-light)"/>
    <path d="M0,328 C200,328 300,312 380,278 C450,250 540,240 700,238 L700,400 L0,400 Z" fill="var(--orange-light)"/>
    <path d="M0,328 C200,328 300,312 380,278 C450,250 540,240 700,238" fill="none" stroke="var(--card-black)" stroke-width="3"/>
  </svg>

  <div class="person">
    <div class="person__name">Adrian Hale</div>
    <div class="person__title">Managing Director</div>
  </div>

  <ul class="contacts">
    <li>
      <svg viewBox="0 0 16 16"><path d="M3 2h3l1 4-2 1a9 9 0 0 0 4 4l1-2 4 1v3a2 2 0 0 1-2 2C6 15 1 10 1 4a2 2 0 0 1 2-2z"/></svg>
      (055) 318 642 907
    </li>
    <li>
      <svg viewBox="0 0 16 16"><path d="M5 1h6a1 1 0 0 1 1 1v12a1 1 0 0 1-1 1H5a1 1 0 0 1-1-1V2a1 1 0 0 1 1-1zm1 2v8h4V3zm2 9a1 1 0 1 0 0 2 1 1 0 0 0 0-2z"/></svg>
      (055)271904836
    </li>
    <li>
      <svg viewBox="0 0 16 16"><path d="M1 4h14v9H1zm1 1 6 4 6-4v-.2H2z" fill-rule="evenodd"/></svg>
      info@velmoralinkway.com
    </li>
  </ul>

  <address class="address">P.O. Box 7384, Grand<br>Rapids, M I 49568</address>

  <div class="brand">
    <div class="brand__dot"></div>
    <div class="brand__name">Velmora Linkway</div>
  </div>

  <div class="website">www.velmoralinkway.com</div>
</section>

</body>
</html>
```